Blog Header Design + 2 Buttons + Colortheme

Hello,
I am looking for a fresh and catchy design for this blog project.
It can have a simplistic touch but I am open to all ideas which fit to the concept.
Please have a look at the pictures I've uploaded.
The website is called
http://www.wtwhn-blog.net
it is a blog which presents weird or extraordinary products. The URL is short for the german phrase "Was Toll Wäre Hier Nun?" it means "How cool is that?". Where "Geil" has the meaning of "Cool".
So yea, that is basically the idea of what it should stand for.
What I need is:
- a colortheme for the website
- a logo or banner at the top of the homesite (see the picture of the text I uploaded, if you could write it in this kind of deign that would look nice I guess)
- buttons for the product elements of the homesite and on the productdetail pages ("Geil!" Button and Price Button/Sign)
- background design (can fit the design idea but shouldnt be too distracting)
- if it is needed by or serves the design, the menu can be changed as well, but it can also stay as it is
optional for a complete set is needed:
- a favicon that fits the theme
- a facebook cover and profile picture
If you have any further questions please let know and I will respond to you as soon as possible.
Again, I am open to ALL design ideas for the whole website concept and would be glad to find a long term deign partner for other projects as well. THANK YOU!

```html
<!DOCTYPE html>
<html lang="de">
<head>
<meta charset="utf-8">
<title>Was Toll Wäre Hier Nun?</title>
<link rel="stylesheet" href="https://fonts.googleapis.com/css2?family=Arimo:wght@400;700&display=swap">
<style>
:root{
  --page-bg:#efefef;
  --site-bg:#e6e6e6;
  --nav-bg:#f7f7f7;
  --nav-active:#e4e4e4;
  --text:#333333;
  --muted:#666666;
  --green:#2f9a3c;
  --green-dark:#2f6b4c;
  --green-light:#7fc7a0;
  --orange:#d2561c;
  --orange-dark:#8e2a0c;
  --card:#ffffff;
  --card-border:#d6d6d6;
}
*{box-sizing:border-box;margin:0;padding:0}
html,body{width:1200px;height:848px;overflow:hidden}
body{background:var(--page-bg);font-family:"Arimo",Arial,sans-serif;color:var(--text);position:relative}
.site{position:absolute;left:188px;top:70px;width:826px;height:666px;background:var(--site-bg);overflow:hidden}
.banner{position:absolute;left:10px;top:0;width:808px;height:89px;
  background:linear-gradient(90deg,#c9b27a 0%,#7fb28a 18%,#3f8c5a 35%,#b9a86a 50%,#6aa37a 65%,#8a9a8a 80%,#2d2d2d 100%);
  display:flex;align-items:center;padding-left:12px}
.brand{font-weight:700;font-size:20px;line-height:22px;color:#ffffff;width:140px}
.nav{position:absolute;left:12px;top:90px;width:802px;height:36px;background:var(--nav-bg);display:flex;align-items:center;padding-left:12px}
.nav a{font-size:11px;color:var(--muted);text-decoration:none;padding:0 11px;height:36px;line-height:36px}
.nav a.active{background:var(--nav-active);color:var(--text)}
.search{margin-left:auto;margin-right:10px;width:150px;height:24px;border:1px solid #cfcfcf;border-radius:3px;background:#fff;display:flex;align-items:center;justify-content:space-between;padding:0 7px;font-size:10px;color:#bbb}
.toolbar{position:absolute;left:12px;top:130px;width:802px;height:24px;display:flex;align-items:center;justify-content:space-between}
.page-title{font-size:17px;font-weight:400;color:var(--text)}
.tools{display:flex;gap:8px;align-items:center;font-size:10px;color:#444}
.grid{position:absolute;left:12px;top:162px;width:802px;display:grid;grid-template-columns:repeat(3,246px);column-gap:32px;row-gap:22px}
.card{background:var(--card);border:1px solid var(--card-border);height:300px;padding:2px}
.card.cut{height:190px;border-bottom:none}
.photo{height:182px;background:linear-gradient(160deg,#e9eef0 0%,#d8e3d8 45%,#c9a98c 70%,#7fb08a 100%)}
.photo.jar{height:188px;background:radial-gradient(ellipse at 50% 55%,#8a4a1a 0%,#c9a24a 40%,#ffffff 72%)}
.photo.legs{height:188px;background:linear-gradient(90deg,#ffffff 10%,#d49a94 30%,#ffffff 50%,#d49a94 70%,#ffffff 90%)}
.photo.kit{height:188px;background:radial-gradient(ellipse at 50% 60%,#d49ad6 0%,#e8c8ea 45%,#ffffff 75%)}
.card h2{font-size:16px;font-weight:400;color:var(--green);text-align:center;margin:14px 0 10px}
.card p{font-size:10.5px;line-height:14px;text-align:justify;padding:0 5px;color:var(--text)}
.more{display:block;text-align:right;font-size:10.5px;color:var(--green);padding:0 5px}
.actions{display:flex;justify-content:space-between;padding:0 1px;margin-top:-2px}
.btn{height:30px;border-radius:7px;color:#fff;font-weight:700;font-size:14px;display:flex;align-items:center;justify-content:flex-end;padding-right:8px}
.btn-geil{width:68px;background:linear-gradient(#7fc7a0,#2f6b4c);border:1px solid #1f4a34}
.btn-price{width:68px;background:linear-gradient(#f08a3a,#8e2a0c);border:1px solid #6a1f08}
.footer{position:absolute;left:0;bottom:0;width:826px;height:30px;background:rgba(240,240,240,.55);text-align:right;padding-right:40px;font-size:10px;line-height:30px;color:var(--green-light)}
.footer span{margin-left:6px}
</style>
</head>
<body>
<main class="site">
  <header class="banner" role="img" aria-label="Farbenfrohe Kopfillustration mit abstrakten grünen, pinken und schwarz-weißen Formen">
    <span class="brand">Was Toll Wäre Hier Nun?</span>
  </header>
  <nav class="nav">
    <a class="active" href="#">Home</a>
    <a href="#">Technik</a>
    <a href="#">Spiel &amp; Spaß</a>
    <a href="#">Kleidung &amp; Accessoires</a>
    <a href="#">Haus &amp; Büro</a>
    <a href="#">Essen &amp; Trinken</a>
    <a href="#">Sonstiges</a>
    <div class="search">Search
      <svg width="11" height="11" viewBox="0 0 12 12"><circle cx="5" cy="5" r="3.8" fill="none" stroke="#666" stroke-width="1.6"/><line x1="8" y1="8" x2="11" y2="11" stroke="#666" stroke-width="1.8"/></svg>
    </div>
  </nav>
  <div class="toolbar">
    <h1 class="page-title">Home</h1>
    <div class="tools">
      <svg width="10" height="10" viewBox="0 0 10 10"><rect x="0.5" y="1.5" width="9" height="8" fill="#3a9a4a"/><rect x="2" y="4" width="6" height="4" fill="#fff"/></svg>
      <svg width="11" height="10" viewBox="0 0 12 10"><path d="M6 10 L1 5 A2.6 2.6 0 0 1 6 2 A2.6 2.6 0 0 1 11 5 Z" fill="#333"/></svg>
      <span>€</span>
      <svg width="10" height="8" viewBox="0 0 10 8"><polyline points="1,7 5,2 9,7" fill="none" stroke="#333" stroke-width="2"/></svg>
      <svg width="10" height="8" viewBox="0 0 10 8"><polyline points="1,1 5,6 9,1" fill="none" stroke="#3a9a4a" stroke-width="2"/></svg>
    </div>
  </div>
  <section class="grid">
    <article class="card">
      <div class="photo" role="img" aria-label="Produktfoto: Kind trinkt durch einen bunten Strohhalm-Bausatz"></div>
      <h2>Strohhalm Bausatz</h2>
      <p>Die Trinkhalm-Pipeline: Bau dir deine eigenen Röhren-Kreationen! Hoch, runter, um die Ecke, bastel eine endlose Reihe...</p>
      <a class="more" href="#">mehr</a>
      <div class="actions"><span class="btn btn-geil">GEIL!</span><span class="btn btn-price">€9,90</span></div>
    </article>
    <article class="card">
      <div class="photo" role="img" aria-label="Produktfoto: Kind trinkt durch einen bunten Strohhalm-Bausatz"></div>
      <h2>Strohhalm Bausatz</h2>
      <p>Die Trinkhalm-Pipeline: Bau dir deine eigenen Röhren-Kreationen! Hoch, runter, um die Ecke, bastel eine endlose Reihe...</p>
      <a class="more" href="#">mehr</a>
      <div class="actions"><span class="btn btn-geil">GEIL!</span><span class="btn btn-price">€9,90</span></div>
    </article>
    <article class="card">
      <div class="photo" role="img" aria-label="Produktfoto: Kind trinkt durch einen bunten Strohhalm-Bausatz"></div>
      <h2>Strohhalm Bausatz</h2>
      <p>Die Trinkhalm-Pipeline: Bau dir deine eigenen Röhren-Kreationen! Hoch, runter, um die Ecke, bastel eine endlose Reihe...</p>
      <a class="more" href="#">mehr</a>
      <div class="actions"><span class="btn btn-geil">GEIL!</span><span class="btn btn-price">€9,90</span></div>
    </article>
    <article class="card cut"><div class="photo jar" role="img" aria-label="Produktfoto: Glas mit Aprikosenaufstrich"></div></article>
    <article class="card cut"><div class="photo legs" role="img" aria-label="Produktfoto: Leggings mit Muskel-Aufdruck"></div></article>
    <article class="card cut"><div class="photo kit" role="img" aria-label="Produktfoto: rosa Werkzeugkoffer"></div></article>
  </section>
  <footer class="footer"><span>AGB</span><span>Impressum</span></footer>
</main>
</body>
</html>
```